Torven Medical needs bold attention catching website for healthcare professionals(target)

I need a hero page as well as a products and about page for a website of mine. I specialize in orthopedic instruments . Specifically bone drills and saws. This whole company was founded to bring superb quality highly discounted medical instruments. Specifically bone drills, bone saws, k-wires and pins. Two main points should be cost savings and superior quality.

Target Market(s)

healthcare professionals Surgeons and hospital material managers

Number of Pages Required

3 page

Font styles to use
Serif

Colors

Designer to choose colors to be used in the design.

Requirements
Must have
• colors should match logo design

```html
<!DOCTYPE html>
<html lang="en">
<head>
<meta charset="utf-8">
<title>Torven Medical</title>
<link href="https://fonts.googleapis.com/css2?family=Lora:wght@400;600;700&family=Mulish:wght@400;600;700;800&display=swap" rel="stylesheet">
<style>
:root{
  --orange:#f7931e;
  --ink:#1b1b1b;
  --dark:#1e1f21;
  --text:#333;
  --light:#f2f2f2;
  --white:#fff;
  --font:'Mulish',sans-serif;
  --serif:'Lora',serif;
}
*{box-sizing:border-box;margin:0;padding:0}
html,body{width:1200px;height:4202px;overflow:hidden}
body{position:relative;font-family:var(--font);color:var(--text);background:var(--white)}
.abs{position:absolute}
.brand{font-family:var(--serif);font-weight:700;color:var(--ink);white-space:nowrap}
.brand.light{color:var(--white)}
.btn{position:absolute;display:flex;align-items:center;justify-content:center;gap:10px;border-radius:30px;font-weight:700;font-size:17px;color:var(--white);background:var(--orange)}
.btn.dark{background:var(--ink)}
.btn .arrow{width:17px;height:17px;border-radius:50%;background:var(--white);display:flex;align-items:center;justify-content:center}
.btn .arrow svg path{stroke:var(--orange)}
.btn.dark .arrow svg path{stroke:var(--ink)}
.section-title{position:absolute;font-family:var(--serif);font-size:36px;font-weight:400;color:var(--ink);white-space:nowrap}
.section-title em{font-style:normal;color:var(--orange);font-weight:600}
.divider{position:absolute;width:220px;height:2px;background:var(--orange)}

.topbar{left:0;top:0;width:1200px;height:42px;background:var(--ink);color:var(--white);font-size:14px}
.topbar .cell{position:absolute;top:0;height:42px;display:flex;align-items:center;gap:6px;padding:0 12px;border-left:1px solid #444;border-right:1px solid #444}
.header{left:0;top:42px;width:1200px;height:110px;background:var(--white)}
.nav{left:0;top:152px;width:1200px;height:65px;background:var(--light);border-top:1px solid #ddd}
.nav a{position:absolute;top:22px;font-size:20px;color:var(--ink);text-decoration:none}
.nav a.active{color:var(--orange)}
.hero{left:0;top:217px;width:1200px;height:680px;overflow:hidden}
.hero-photo{position:absolute;inset:0;background:linear-gradient(100deg,#2f8fd0 0%,#8cc8ea 35%,#d9d3cf 55%,#f0a070 80%,#e36a30 100%)}
.copy{position:absolute;font-size:17px;line-height:36px;color:var(--text)}
.hr{left:90px;top:1310px;width:1020px;height:1px;background:#e4e4e4}
.info-icon{position:absolute;width:84px;height:84px;border-radius:50%;background:var(--orange);display:flex;align-items:center;justify-content:center}
.info-text{position:absolute;width:320px;text-align:center;font-size:18px;line-height:28px;color:#555}
.field{position:absolute;height:40px;border:1px solid #eee;box-shadow:0 2px 0 #e2e2e2;font-size:12px;color:#555;padding:11px 16px}
.footer-col h4{position:absolute;font-size:15px;font-weight:700;color:var(--white)}
.footer-col a{position:absolute;font-size:14px;color:#ccc;text-decoration:none}
.social{position:absolute;top:3873px;width:28px;height:28px;border:1.5px solid #ddd;border-radius:50%}
</style>
</head>
<body>

<div class="abs topbar">
  <div class="cell" style="left:90px">
    <svg width="16" height="12" viewBox="0 0 16 12"><rect x="1" y="1" width="14" height="10" fill="none" stroke="#fff" stroke-width="1.6"/><path d="M1 1l7 6 7-6" fill="none" stroke="#fff" stroke-width="1.6"/></svg>
    info@torvenmedical.com
  </div>
  <div class="cell" style="right:90px;font-size:12.5px">
    <svg width="10" height="14" viewBox="0 0 10 14"><path d="M5 0a5 5 0 0 0-5 5c0 4 5 9 5 9s5-5 5-9a5 5 0 0 0-5-5z" fill="#fff"/><circle cx="5" cy="5" r="2" fill="#1b1b1b"/></svg>
    4820 Harlow Parkway, Suite 210, Brenton, TX 75990
  </div>
</div>

<div class="abs header">
  <svg class="abs" style="left:202px;top:32px" width="44" height="44" viewBox="0 0 44 44">
    <circle cx="22" cy="22" r="19" fill="none" stroke="#f7931e" stroke-width="3"/>
    <path d="M15 13c-2 2-1 6 3 11s8 8 11 7l2-3-4-3-2 2c-2-1-5-4-6-6l2-2-3-4z" fill="#f7931e"/>
  </svg>
  <div class="abs" style="left:254px;top:30px;font-size:15px;color:var(--orange)">Call us:</div>
  <div class="abs" style="left:254px;top:52px;font-size:18px;font-weight:700;color:var(--ink)">(800) 555-0147</div>
  <div class="abs brand" style="left:600px;top:38px;transform:translateX(-50%);font-size:32px">Torven Medical</div>
  <div class="btn" style="left:806px;top:28px;width:205px;height:54px;font-size:16px">
    <svg width="14" height="15" viewBox="0 0 14 15"><circle cx="7" cy="4" r="3.6" fill="#fff"/><path d="M0 15c0-5 3-7 7-7s7 2 7 7z" fill="#fff"/></svg>
    Login Portal
  </div>
</div>

<nav class="abs nav">
  <a class="active" style="left:115px">HOME</a>
  <a style="left:235px">ABOUT US</a>
  <a style="left:393px">OUR PRODUCTS</a>
  <a style="left:602px">TESTIMONIALS</a>
  <a style="left:798px">OUR BLOG</a>
  <a style="left:959px">CONTACT US</a>
</nav>

<section class="abs hero">
  <div class="hero-photo" role="img" aria-label="Surgeon in gloves holding an orthopedic instrument in an operating room"></div>
  <svg class="abs" style="left:0;top:0" width="1200" height="680" viewBox="0 0 1200 680">
    <path d="M0 540 C200 680 560 660 1200 450 L1200 680 L0 680 Z" fill="#f7931e"/>
    <path d="M0 565 C220 700 600 650 1200 490 L1200 680 L0 680 Z" fill="#fff"/>
  </svg>
  <div class="abs brand" style="left:864px;top:130px;transform:translateX(-50%);font-size:34px">Torven Medical</div>
  <div class="abs" style="left:610px;top:236px;font-size:27px;font-weight:700;color:var(--white)">COST SAVINGS &amp; SUPERIOR QUALITY.</div>
  <div class="btn" style="left:649px;top:290px;width:206px;height:54px">Read More <span class="arrow"><svg width="9" height="9" viewBox="0 0 9 9"><path d="M1 4.5h6M4.5 2l2.5 2.5L4.5 7" fill="none" stroke-width="1.8"/></svg></span></div>
  <div class="btn dark" style="left:868px;top:290px;width:206px;height:54px">Our Products <span class="arrow"><svg width="9" height="9" viewBox="0 0 9 9"><path d="M1 4.5h6M4.5 2l2.5 2.5L4.5 7" fill="none" stroke-width="1.8"/></svg></span></div>
</section>

<section class="welcome">
  <h1 class="section-title" style="left:0;width:1200px;text-align:center;top:950px">Welcome to <em>Torven Medical</em></h1>
  <div class="divider" style="left:490px;top:1021px"></div>
  <p class="copy" style="left:140px;width:920px;top:1046px;text-align:center">Our instruments meet the demands of the operating room without the premium price. From bone drills to saws, k-wires and pins, every product is built to strict standards so surgeons can rely on it case after case, while your budget goes much further.</p>
  <div class="btn" style="left:388px;top:1174px;width:206px;height:56px">Read More <span class="arrow"><svg width="9" height="9" viewBox="0 0 9 9"><path d="M1 4.5h6M4.5 2l2.5 2.5L4.5 7" fill="none" stroke-width="1.8"/></svg></span></div>
  <div class="btn dark" style="left:607px;top:1174px;width:206px;height:56px">Our Products <span class="arrow"><svg width="9" height="9" viewBox="0 0 9 9"><path d="M1 4.5h6M4.5 2l2.5 2.5L4.5 7" fill="none" stroke-width="1.8"/></svg></span></div>
</section>

<div class="abs hr"></div>

<section class="about">
  <div class="abs brand" style="left:90px;top:1530px;width:500px;font-size:52px;display:flex;align-items:center;gap:16px">
    <span style="display:inline-block;width:24px;height:24px;border-radius:50%;background:var(--orange)"></span>Torven Medical
  </div>
  <h2 class="section-title" style="left:617px;top:1380px">About <em>Torven Medical</em></h2>
  <div class="divider" style="left:617px;top:1446px"></div>
  <p class="copy" style="left:617px;width:495px;top:1462px;font-size:15.5px;text-align:justify">Torven Medical was founded to bring superb quality orthopedic instruments to hospitals at a highly discounted price. We focus on bone drills, bone saws, k-wires and pins, working closely with surgeons and material managers to cut costs without compromise.</p>
  <div class="btn" style="left:617px;top:1690px;width:206px;height:54px">Read More <span class="arrow"><svg width="9" height="9" viewBox="0 0 9 9"><path d="M1 4.5h6M4.5 2l2.5 2.5L4.5 7" fill="none" stroke-width="1.8"/></svg></span></div>
</section>

<section class="abs" style="left:0;top:1830px;width:1200px;height:940px">
  <svg class="abs" style="left:0;top:0" width="1200" height="940" viewBox="0 0 1200 940">
    <defs>
      <linearGradient id="prodBg" x1="0" y1="0" x2="1" y2="1">
        <stop offset="0" stop-color="#2a2c2f"/><stop offset=".5" stop-color="#34383d"/><stop offset="1" stop-color="#26282b"/>
      </linearGradient>
    </defs>
    <path d="M0 200 C400 90 800 20 1200 110 L1200 230 L0 230 Z" fill="#f7931e"/>
    <path d="M0 220 C420 120 800 50 1200 140 L1200 720 C900 800 500 840 300 830 C150 822 60 800 0 790 Z" fill="url(#prodBg)" role="img" aria-label="Darkened photo of surgeons at work in an operating theatre"/>
    <path d="M0 790 C60 800 150 822 300 830 C500 840 900 800 1200 720 L1200 750 C900 850 500 930 260 920 C120 912 40 880 0 850 Z" fill="#f7931e"/>
  </svg>
  <h2 class="section-title" style="left:90px;top:285px;color:var(--white)">Our <b style="font-weight:700">Product</b></h2>
  <div class="divider" style="left:90px;top:350px"></div>
  <div class="abs" style="left:666px;top:239px;width:446px;height:446px;border-radius:50%;border:6px solid var(--orange);background:var(--dark)"></div>
  <div class="abs" role="img" aria-label="Orthopedic drill bits standing on a white and orange geometric backdrop" style="left:682px;top:255px;width:414px;height:414px;border-radius:50%;background:linear-gradient(135deg,#f2f2f2 0%,#dfe3e6 40%,#f5b070 60%,#eef0f2 80%,#ffffff 100%)"></div>
</section>
<p class="copy" style="left:90px;width:496px;top:2200px;font-size:16px;text-align:justify;color:var(--white)">Precision bone drills, oscillating saws, k-wires and pins engineered for consistent performance in the operating room, offered at prices that help hospitals stretch every budget further. Built for surgeons who expect reliability every case.</p>
<div class="btn" style="left:90px;top:2391px;width:251px;height:56px">View More Products <span class="arrow"><svg width="9" height="9" viewBox="0 0 9 9"><path d="M1 4.5h6M4.5 2l2.5 2.5L4.5 7" fill="none" stroke-width="1.8"/></svg></span></div>

<section class="contact">
  <h2 class="section-title" style="left:0;width:1200px;text-align:center;top:2822px;color:var(--orange);font-weight:600">Contact Information</h2>
  <div class="divider" style="left:490px;top:2886px"></div>
  <div class="abs" style="left:0;width:1200px;text-align:center;top:2910px;font-size:21px;color:#444">Contact us for more information</div>

  <div class="info-icon" style="left:261px;top:2954px"><svg width="40" height="44" viewBox="0 0 40 44"><path d="M20 3a12 12 0 0 0-12 12c0 9 12 21 12 21s12-12 12-21A12 12 0 0 0 20 3z" fill="none" stroke="#fff" stroke-width="2"/><circle cx="20" cy="15" r="4.5" fill="none" stroke="#fff" stroke-width="2"/><ellipse cx="20" cy="39" rx="14" ry="3" fill="none" stroke="#fff" stroke-width="2"/></svg></div>
  <div class="info-icon" style="left:553px;top:2954px"><svg width="42" height="42" viewBox="0 0 42 42"><path d="M10 5l7 8-4 5c2 5 6 9 11 11l5-4 8 7-4 5c-12 1-27-14-27-27z" fill="none" stroke="#fff" stroke-width="2" stroke-linejoin="round"/></svg></div>
  <div class="info-icon" style="left:873px;top:2954px"><svg width="46" height="32" viewBox="0 0 46 32"><rect x="2" y="2" width="42" height="28" fill="none" stroke="#fff" stroke-width="2"/><path d="M2 2l21 16L44 2M2 30l16-14M44 30L28 16" fill="none" stroke="#fff" stroke-width="2"/></svg></div>

  <div class="info-text" style="left:143px;top:3047px">4820 Harlow Parkway, Suite 210,<br>Brenton, TX 75990</div>
  <div class="info-text" style="left:435px;top:3047px">Phone:<br>+1 (800) 555-0147</div>
  <div class="info-text" style="left:755px;top:3052px">Email:<br>info@torvenmedical.com</div>

  <h2 class="section-title" style="left:0;width:1200px;text-align:center;top:3128px;color:var(--orange);font-weight:600">Contact Us</h2>
  <div class="divider" style="left:490px;top:3192px"></div>

  <div class="field" style="left:161px;top:3229px;width:430px">&#9679; First Name</div>
  <div class="field" style="left:608px;top:3229px;width:431px">&#9679; Last Name</div>
  <div class="field" style="left:161px;top:3284px;width:430px">&#9632; Company</div>
  <div class="field" style="left:161px;top:3338px;width:430px">&#9993; Email Address</div>
  <div class="field" style="left:161px;top:3393px;width:430px">&#9742; Phone Number</div>
  <div class="field" style="left:608px;top:3284px;width:431px;height:150px">&#9632; Message :</div>
  <div class="btn" style="left:497px;top:3451px;width:206px;height:54px">
    <svg width="16" height="16" viewBox="0 0 16 16"><path d="M0 7L16 0 12 16 8 10z" fill="#fff"/></svg>Submit
  </div>
</section>

<footer>
  <svg class="abs" style="left:0;top:3570px" width="1200" height="632" viewBox="0 0 1200 632">
    <path d="M0 220 C300 80 800 -30 1200 90 L1200 632 L0 632 Z" fill="#f7931e"/>
    <path d="M0 215 C320 110 820 40 1200 120 L1200 632 L0 632 Z" fill="#1b1b1b"/>
  </svg>
  <div class="abs brand light" style="left:90px;top:3842px;font-size:28px">Torven Medical</div>
  <div class="abs" style="left:832px;top:3878px;font-size:14px;font-weight:700;color:var(--white)">FOLLOW US :</div>
  <div class="social" style="left:937px"></div>
  <div class="social" style="left:972px"></div>
  <div class="social" style="left:1007px"></div>
  <div class="social" style="left:1042px"></div>
  <div class="social" style="left:1077px"></div>
  <div class="abs" style="left:80px;top:3918px;width:1045px;height:1px;background:#3a3a3a"></div>

  <div class="footer-col">
    <h4 style="left:91px;top:3949px">NAVIGATION</h4>
    <a style="left:91px;top:3987px">Home</a><a style="left:189px;top:3985px">Shop</a>
    <a style="left:91px;top:4014px">About</a><a style="left:189px;top:4012px">Blog</a>
    <a style="left:91px;top:4041px">Products</a><a style="left:189px;top:4039px">Contact</a>
    <a style="left:91px;top:4068px">Testimonials</a>

    <h4 style="left:333px;top:3949px">LINKS</h4>
    <a style="left:333px;top:3987px">Terms &amp; Conditions</a>
    <a style="left:333px;top:4014px">Privacy Policy</a>
    <a style="left:333px;top:4041px">Site Map</a>
    <a style="left:333px;top:4068px">Disclaimer</a>

    <h4 style="left:558px;top:3949px">CONTACT INFO</h4>
    <a style="left:580px;top:3985px;font-size:13px;line-height:24px">4820 Harlow Parkway, Suite 210,<br>Brenton, TX 75990</a>
    <a style="left:558px;top:4045px;font-size:13.5px">&#9742; Help :800 555 0147</a>
    <a style="left:558px;top:4082px;font-size:13.5px">&#9993; info@torvenmedical.com</a>

    <h4 style="left:835px;top:3949px">NEWSLETTER</h4>
    <div class="abs" style="left:836px;top:3988px;width:275px;height:38px;background:#fff;border-radius:3px;font-size:11px;color:#999;padding:12px 14px">Enter e-mail address</div>
    <div class="btn" style="left:836px;top:4043px;width:154px;height:40px;font-weight:600">Subscribe</div>
  </div>

  <div class="abs" style="left:0;width:1200px;text-align:center;top:4162px;font-size:12px;color:#999">Copyrights&copy; Torven Medical 2019 | Allrights Reserved.</div>
</footer>

</body>
</html>
```